Golden Years Wellness Roadmap: This is my second book. The first was Eldercare Compass

I need a book cover design for: GOLDEN YEARS WELLNESS ROADMAP: A NO-EXPENSE METHOD FOR FINISHING YOUR LATER-LIFE MOSAIC WITH POOLED KVB CARE SCHEMES by Derek Holloway Neil Osgrove & Martin Quarles. This book is designed for business owners, CEO's, CFO's and Human Resources. The cover needs to be professional and focused on business. The purpose of this book is to educate business owners and their management about a zero cost retiree health plan. This is a first of it's kind solution that every business needs to learn about.

Target Market(s)

Business owners, CEO's, CFO's and Human Resources

Requirements
Nice to have
• I want the design to be clean and professional since it is focused on business executives

```html
<!DOCTYPE html>
<html lang="en">
<head>
<meta charset="utf-8">
<title>Golden Years Wellness Roadmap — Book Cover</title>
<link rel="stylesheet" href="https://fonts.googleapis.com/css2?family=Oswald:wght@300;400&family=Montserrat:wght@400;500;600&display=swap">
<style>
  :root {
    --navy-deep: #0a1838;
    --navy: #0f2250;
    --blue-mid: #1d4fa6;
    --blue-bright: #2f7ae0;
    --blue-title: #3fa3f0;
    --white: #ffffff;
    --rule: rgba(120, 170, 240, 0.35);
  }
  * { margin: 0; padding: 0; box-sizing: border-box; }
  html, body {
    width: 800px;
    height: 1200px;
    overflow: hidden;
    background: var(--navy-deep);
  }
  .cover {
    position: relative;
    width: 800px;
    height: 1200px;
    background: radial-gradient(ellipse at 50% 45%, var(--navy) 0%, var(--navy-deep) 75%);
    overflow: hidden;
    color: var(--white);
    text-align: center;
  }
  .tiles {
    position: absolute;
    left: 0;
    width: 800px;
    display: block;
  }
  .tiles--top { top: 0; height: 300px; }
  .tiles--bottom { bottom: 0; height: 330px; }
  .subtitle {
    position: absolute;
    top: 208px;
    left: 0;
    width: 100%;
    font-family: "Montserrat", sans-serif;
    font-weight: 500;
    font-size: 16px;
    line-height: 24px;
    letter-spacing: 1.5px;
    text-transform: uppercase;
  }
  .rule {
    position: absolute;
    left: 0;
    width: 800px;
    height: 1px;
    background: var(--rule);
  }
  .rule--upper { top: 332px; }
  .rule--lower { top: 585px; }
  .title {
    position: absolute;
    top: 360px;
    left: 0;
    width: 100%;
    font-family: "Oswald", sans-serif;
    font-weight: 300;
    text-transform: uppercase;
  }
  .title__lead {
    display: block;
    font-size: 58px;
    line-height: 70px;
    letter-spacing: 3px;
    color: var(--white);
  }
  .title__main {
    display: block;
    font-size: 116px;
    line-height: 128px;
    letter-spacing: 6px;
    color: var(--blue-title);
  }
  .authors {
    position: absolute;
    top: 618px;
    left: 0;
    width: 100%;
    font-family: "Montserrat", sans-serif;
    font-weight: 500;
    font-size: 21px;
    line-height: 34px;
    letter-spacing: 2px;
    text-transform: uppercase;
  }
</style>
</head>
<body>
  <main class="cover">
    <svg class="tiles tiles--top" viewBox="0 0 800 300" role="img" aria-label="Blue jigsaw puzzle pieces scattered across the top edge">
      <defs>
        <linearGradient id="topFade" x1="0" y1="0" x2="0" y2="1">
          <stop offset="0" stop-color="#1d4fa6" stop-opacity="0.95"/>
          <stop offset="0.45" stop-color="#173f8a" stop-opacity="0.6"/>
          <stop offset="1" stop-color="#0a1838" stop-opacity="0"/>
        </linearGradient>
      </defs>
      <rect width="800" height="300" fill="url(#topFade)"/>
    </svg>

    <p class="subtitle">A no-expense method<br>for finishing your later-life<br>mosaic with pooled KVB care schemes</p>

    <div class="rule rule--upper"></div>
    <h1 class="title">
      <span class="title__lead">Golden Years Wellness</span>
      <span class="title__main">Roadmap</span>
    </h1>
    <div class="rule rule--lower"></div>

    <p class="authors">Derek Holloway, Neil Osgrove<br>Martin Quarles</p>

    <svg class="tiles tiles--bottom" viewBox="0 0 800 330" role="img" aria-label="Blue jigsaw puzzle pieces gathered along the bottom edge">
      <defs>
        <linearGradient id="bottomFade" x1="0" y1="1" x2="0" y2="0">
          <stop offset="0" stop-color="#2f7ae0" stop-opacity="0.95"/>
          <stop offset="0.5" stop-color="#1d4fa6" stop-opacity="0.6"/>
          <stop offset="1" stop-color="#0a1838" stop-opacity="0"/>
        </linearGradient>
      </defs>
      <rect width="800" height="330" fill="url(#bottomFade)"/>
    </svg>
  </main>
</body>
</html>
```